Images and design ideas provided: Postcard size flier

2 sided postcard size flier to hand people on the street.

A FUN tax business needs a postcard size flier to hand people on the street. Not a typical serious, quiet, office so make the image fun!

Exact wording, logo and key images provided. You are free to add other images as you see fit (such as money).

Side 1: Use image of lady looking up (she should be looking at text provided).All spanish and english text provided. Logo in bottom right corner. Address at bottom of card.

Side 2: Image of lady holding money and pointing. Remove money and have her holding a sign/or some other creative way to have her looking at text. All spanish and english text provided. Logo in bottom right corner. Address at bottom of card.

Size: 4" x 6" horizontal or vertical is ok
Each side can be different and image/design does not have to be related.

Target Market(s)

Age 18-35

Industry/Entity Type

Accounting

Font styles to use
Sans Serif

Colors

Designer to choose colors to be used in the design.

Requirements
Must have
• Use text document provided. All text goes on both sides.
• Should be easy to read from a few feet away.
Nice to have
• Bright colors to attract attention of people walking by to grab flier/card. Images of money ok.
Should not have
• No images of calculators or typical accounting tax forms.

```html
<!DOCTYPE html>
<html lang="en">
<head>
<meta charset="utf-8">
<title>Refund Royale – Postcard Flier</title>
<link href="https://fonts.googleapis.com/css2?family=Noto+Serif:wght@700&family=PT+Sans:wght@400;700&display=swap" rel="stylesheet">
<style>
  :root {
    --red: #d41c24;
    --red-dark: #8e1b1f;
    --yellow: #f2cc0f;
    --gold: #f3c21a;
    --grey: #8d8d8d;
    --paper: #f4f4f4;
    --white: #ffffff;
    --ink: #1d1d1d;
    --stage: #e4e4e4;
    --robe-green: #8a8f62;
    --robe-red: #a8312c;
  }
  * { box-sizing: border-box; margin: 0; padding: 0; }
  html, body { width: 1200px; height: 951px; overflow: hidden; background: var(--stage); }
  .canvas { position: relative; width: 1200px; height: 951px; }

  .postcard {
    position: absolute; left: 270px; width: 660px; height: 440px;
    background: var(--paper); overflow: hidden;
    box-shadow: 0 6px 18px rgba(0,0,0,.18);
    font-family: "PT Sans", sans-serif;
  }
  .postcard--front { top: 25px; }
  .postcard--back { top: 486px; }
  .postcard svg.shapes { position: absolute; inset: 0; }

  .serif { font-family: "Noto Serif", serif; font-weight: 700; }
  .abs { position: absolute; }
  .photo { position: absolute; }

  /* side 1 */
  .front-headline { left: 26px; top: 26px; font-size: 36px; color: var(--red); white-space: nowrap; }
  .ribbon-text { left: 30px; top: 84px; font-size: 15px; font-weight: 700; color: var(--ink); }
  .front-photo { left: 30px; top: 112px; width: 270px; height: 244px;
    background: linear-gradient(180deg, #ecebe8 0%, #c9b9a0 35%, var(--robe-green) 70%, var(--robe-red) 100%); }
  .front-phone { left: 90px; top: 370px; font-size: 18px; color: var(--ink); display: flex; align-items: center; gap: 8px; }
  .front-address { left: 14px; top: 409px; font-size: 15px; color: var(--white); display: flex; align-items: center; gap: 6px; }
  .front-spanish { left: 410px; top: 150px; width: 230px; text-align: center; color: var(--gold); }
  .front-spanish .lead { font-size: 27px; }
  .front-spanish .amount { font-size: 52px; line-height: 1.05; }
  .front-spanish .rest { font-size: 28px; line-height: 1.15; }
  .front-spanish-sub { left: 400px; top: 330px; width: 250px; text-align: center; font-size: 18px; line-height: 1.3; color: var(--white); }
  .brand { display: flex; align-items: center; gap: 10px; font-weight: 700; text-transform: uppercase; letter-spacing: 1px; white-space: nowrap; }
  .brand .mark { width: 14px; height: 14px; border-radius: 50%; flex: none; }
  .front-brand { left: 440px; top: 394px; font-size: 24px; color: var(--white); }
  .front-brand .mark { background: var(--white); }

  /* side 2 */
  .back-photo { left: 20px; top: 86px; width: 250px; height: 300px;
    background: linear-gradient(180deg, #c44a3f 0%, #d9b58f 30%, var(--robe-green) 65%, var(--robe-red) 100%); }
  .back-headline { left: 300px; top: 46px; font-size: 24px; color: var(--gold); white-space: nowrap; }
  .back-ribbon { left: 410px; top: 80px; font-size: 11px; font-weight: 700; color: var(--white); }
  .back-spanish { left: 330px; top: 96px; font-size: 19px; line-height: 1.15; color: var(--gold); }
  .back-sub { left: 380px; top: 160px; width: 270px; text-align: center; font-size: 15px; font-weight: 700; line-height: 1.15; color: var(--ink); }
  .back-brand { left: 420px; top: 258px; font-size: 28px; color: var(--red); }
  .back-brand .mark { background: #2b5fb0; }
  .back-info { left: 0; top: 396px; width: 660px; height: 44px; display: flex; justify-content: space-around; align-items: center; font-size: 14px; color: var(--white); }
  .back-info span { display: flex; align-items: center; gap: 6px; }
</style>
</head>
<body>
<main class="canvas">

  <section class="postcard postcard--front">
    <svg class="shapes" width="660" height="440" viewBox="0 0 660 440">
      <defs>
        <linearGradient id="frontRed" x1="0" y1="0" x2="1" y2="1">
          <stop offset="0" stop-color="#e3222b"/><stop offset="1" stop-color="#8e1b1f"/>
        </linearGradient>
      </defs>
      <polygon points="410,0 490,0 440,90" fill="#8d8d8d"/>
      <polygon points="495,0 660,0 660,440 285,440" fill="url(#frontRed)"/>
      <polygon points="0,70 310,70 300,86 310,102 0,102" fill="var(--yellow)"/>
      <polygon points="0,360 305,360 292,400 0,400" fill="var(--yellow)"/>
      <polygon points="0,400 292,400 280,440 0,440" fill="#8d8d8d"/>
    </svg>
    <h1 class="abs serif front-headline">Get $100 Cash Now!</h1>
    <p class="abs ribbon-text">WITH PAID TAX PREPARATION</p>
    <div class="photo front-photo" role="img" aria-label="Photo of a smiling woman in a king costume looking up with arms raised as banknotes fall around her"></div>
    <p class="abs front-phone">
      <svg width="16" height="16" viewBox="0 0 24 24"><path fill="#1d1d1d" d="M6.6 10.8a15 15 0 0 0 6.6 6.6l2.2-2.2a1 1 0 0 1 1-.3 11 11 0 0 0 3.6.6 1 1 0 0 1 1 1V20a1 1 0 0 1-1 1A17 17 0 0 1 3 4a1 1 0 0 1 1-1h3.5a1 1 0 0 1 1 1 11 11 0 0 0 .6 3.6 1 1 0 0 1-.3 1z"/></svg>
      (555) 014-2290
    </p>
    <p class="abs front-address">
      <svg width="12" height="14" viewBox="0 0 24 28"><path fill="#d41c24" d="M12 0a10 10 0 0 0-10 10c0 7 10 18 10 18s10-11 10-18A10 10 0 0 0 12 0zm0 14a4 4 0 1 1 0-8 4 4 0 0 1 0 8z"/></svg>
      418 Harbor Ave. Eastdale NY 10000
    </p>
    <div class="abs serif front-spanish">
      <p class="lead">Reciba</p>
      <p class="amount">$100</p>
      <p class="rest">en efectivo<br>ahora!</p>
    </div>
    <p class="abs front-spanish-sub">con la preparacion<br>pagada de sus impuestos</p>
    <p class="abs brand front-brand"><span class="mark"></span>Refund Royale</p>
  </section>

  <section class="postcard postcard--back">
    <svg class="shapes" width="660" height="440" viewBox="0 0 660 440">
      <polygon points="0,0 150,0 330,396 0,396" fill="var(--red)"/>
      <polygon points="150,0 240,0 195,70" fill="#8d8d8d"/>
      <polygon points="285,30 650,30 650,200 330,200" fill="var(--red)"/>
      <polygon points="330,150 660,150 660,200 350,200" fill="var(--yellow)"/>
      <rect x="0" y="396" width="660" height="44" fill="#8d8d8d"/>
    </svg>
    <div class="photo back-photo" role="img" aria-label="Photo of a woman in a king costume pointing toward the offer text"></div>
    <h2 class="abs serif back-headline">Get $100 Cash Now!</h2>
    <p class="abs back-ribbon">WITH PAID TAX PREPARATION</p>
    <p class="abs serif back-spanish">Reciba $100<br>en efectivo ahora!</p>
    <p class="abs back-sub">con la preparacion pagada<br>de sus impuestos</p>
    <p class="abs brand back-brand"><span class="mark"></span>Refund Royale</p>
    <div class="abs back-info">
      <span><svg width="12" height="14" viewBox="0 0 24 28"><path fill="#d41c24" d="M12 0a10 10 0 0 0-10 10c0 7 10 18 10 18s10-11 10-18A10 10 0 0 0 12 0zm0 14a4 4 0 1 1 0-8 4 4 0 0 1 0 8z"/></svg>418 Harbor Ave. Eastdale NY 10000</span>
      <span><svg width="13" height="13" viewBox="0 0 24 24"><path fill="#d41c24" d="M6.6 10.8a15 15 0 0 0 6.6 6.6l2.2-2.2a1 1 0 0 1 1-.3 11 11 0 0 0 3.6.6 1 1 0 0 1 1 1V20a1 1 0 0 1-1 1A17 17 0 0 1 3 4a1 1 0 0 1 1-1h3.5a1 1 0 0 1 1 1 11 11 0 0 0 .6 3.6 1 1 0 0 1-.3 1z"/></svg>(555) 014-2290</span>
      <span><svg width="13" height="13" viewBox="0 0 24 24"><circle cx="12" cy="12" r="10" fill="none" stroke="#d41c24" stroke-width="3"/><path d="M2 12h20M12 2c4 4 4 16 0 20M12 2c-4 4-4 16 0 20" fill="none" stroke="#d41c24" stroke-width="2"/></svg>refundroyale.example</span>
    </div>
  </section>

</main>
</body>
</html>
```